Business Card Design Project

We need a business card design for a immigration & education centre , we majoy help student with their visa and migration to australia . this is our home page . www.quorelpath.com.au
we prefer use the designer named Danu Weskatra the design with the QR code [Linked to Design #518099] is the way we want it done .
for further information please contact me
thanks
Reason: since the office is closed for holidays , i havent check my email often , so extend the dearline for a week ~
Hurry up great designers , the project will be end at end of this week .
looking forward to see you wonderful design !!!
Industry/Entity Type
Education
Look and feel
Each slider illustrates characteristics of the customer's brand and the style your logo design should communicate.

```html
<!DOCTYPE html>
<html lang="en">
<head>
<meta charset="utf-8">
<title>QuorelPath Business Card</title>
<link rel="stylesheet" href="https://fonts.googleapis.com/css2?family=Marcellus&display=swap">
<style>
  :root {
    --page: #e9e4de;
    --card-green: #22361a;
    --card-dark: #0b0d09;
    --ink: #f4f1ea;
    --accent: #d8231c;
  }
  * { margin: 0; padding: 0; box-sizing: border-box; }
  html, body { width: 846px; height: 1200px; overflow: hidden; }
  body {
    background: var(--page);
    font-family: "Marcellus", serif;
    color: var(--ink);
    position: relative;
  }
  .card {
    position: absolute;
    left: 143px;
    width: 560px;
    height: 320px;
    background: linear-gradient(150deg, var(--card-green) 0%, var(--card-green) 30%, var(--card-dark) 52%, var(--card-green) 72%, var(--card-green) 100%);
    box-shadow: 0 6px 16px rgba(0,0,0,0.3);
  }
  .card--front { top: 170px; }
  .card--back { top: 620px; }

  .brand { position: absolute; text-align: center; }
  .brand__mark {
    display: inline-flex; align-items: center; gap: 10px;
  }
  .brand__dot {
    width: 16px; height: 16px; border-radius: 50%; background: var(--accent);
  }
  .brand__name { font-size: 44px; line-height: 1; color: var(--ink); }
  .brand__tagline { font-size: 16px; margin-top: 6px; letter-spacing: 0.3px; }

  .card--front .brand { left: 130px; top: 110px; width: 300px; }
  .card--front .website {
    position: absolute; left: 0; right: 0; bottom: 30px;
    text-align: center; font-size: 18px; letter-spacing: 0.5px;
  }

  .card--back .website {
    position: absolute; right: 26px; top: 20px; font-size: 17px;
  }
  .card--back .brand { right: 26px; top: 110px; width: 250px; }
  .card--back .brand__name { font-size: 34px; }
  .card--back .brand__dot { width: 12px; height: 12px; }
  .card--back .brand__tagline { font-size: 13px; }

  .person { position: absolute; left: 22px; top: 20px; }
  .person__name { font-size: 28px; line-height: 1; }
  .person__role { font-size: 13px; margin-left: 24px; margin-top: 3px; }
  .person__reg { font-size: 8px; margin-left: 24px; margin-top: 1px; }

  .contact {
    position: absolute; left: 22px; top: 112px;
    list-style: none; font-size: 13px; line-height: 1.45;
  }
  .contact .contact__marn { font-size: 9px; margin-bottom: 3px; }
  .contact .contact__gap { margin-top: 5px; }
  .contact .contact__qq { font-size: 9px; margin-top: 7px; }

  .social {
    position: absolute; right: 26px; bottom: 60px;
    text-align: right; font-size: 9px; line-height: 1.25;
  }
</style>
</head>
<body>

<section class="card card--front" aria-label="Business card front">
  <div class="brand">
    <div class="brand__mark">
      <span class="brand__dot"></span>
      <span class="brand__name">QuorelPath</span>
    </div>
    <p class="brand__tagline">Immigration &amp; Education Centre</p>
  </div>
  <p class="website">www.quorelpath.com.au</p>
</section>

<section class="card card--back" aria-label="Business card back">
  <p class="website">www.quorelpath.com.au</p>

  <div class="person">
    <h1 class="person__name">Marlon Teague</h1>
    <p class="person__role">Managing Director</p>
    <p class="person__reg">Registered Migration Agent</p>
  </div>

  <ul class="contact">
    <li class="contact__marn">MARN: 0417293</li>
    <li>Address: Suite 804 Level 8,</li>
    <li>212 Harlow St, Melbourne VIC 3000</li>
    <li class="contact__gap">Phone: (03) 9411 2650</li>
    <li>Direct: (03) 9411 2651</li>
    <li>Fax: +61 3 9417 6203</li>
    <li>Email: marlon.teague@quorelpath.com.au</li>
    <li>Free Call: 1800 QP PATH (1800 77 7284)</li>
    <li>Mobile: 0455 21 PATH (0455 21 7284)</li>
    <li class="contact__qq">QQ: 3057194426</li>
  </ul>

  <div class="brand">
    <div class="brand__mark">
      <span class="brand__dot"></span>
      <span class="brand__name">QuorelPath</span>
    </div>
    <p class="brand__tagline">Immigration &amp; Education Centre</p>
  </div>

  <div class="social">
    <p>SKYPE: QuorelPath_Melbourne</p>
    <p>facebook.com/quorelpath</p>
    <p>twitter.com/quorelpath</p>
  </div>
</section>

</body>
</html>
```